Product Introduction Brochure

Brochure to introduce our mid/high end lighting products to potential wholesalers / Disrtibutors / Retailers. To be mainly graphical but will contain some text also. The purpose of the brochure will be to get potential customers to find out more either by calling us or to visit our website. The brochure should be of A3 size folded in half to an A4. Front page should be mainly logo and name, inner 2 pages should showcase some of the products we can supply together with some text (to be supplied, please use filler text in the initial design), then the back page containing our contact details. The products are lights, floor lamps and table lamps. I have attached a number of images, as well as our company logo. I would prefer the design to be on a black background, however this is not critical
Target Market(s)
Retailer, distribution and wholesale buyers
Interior design consultants and specifiers
Industry/Entity Type
Product
Look and feel
Each slider illustrates characteristics of the customer's brand and the style your logo design should communicate.

```html
<!DOCTYPE html>
<html lang="en">
<head>
<meta charset="utf-8">
<title>Lumivo Product Brochure – Cover Spread</title>
<link rel="stylesheet" href="https://fonts.googleapis.com/css2?family=Montserrat:wght@400;700&display=swap">
<style>
  :root {
    --page-bg: #d9d9d9;
    --sheet-black: #050505;
    --sphere-light: #2b2f33;
    --sphere-dark: #0c0d0e;
    --brand-green: #3fae4a;
    --contact-grey: #9a9a9a;
    --fold-line: #151515;
  }
  * { margin: 0; padding: 0; box-sizing: border-box; }
  html, body {
    width: 1200px;
    height: 800px;
    overflow: hidden;
    background: var(--page-bg);
  }
  .canvas {
    position: relative;
    width: 1200px;
    height: 800px;
  }
  .spread {
    position: absolute;
    left: 60px;
    top: 18px;
    width: 1080px;
    height: 764px;
    background: var(--sheet-black);
    overflow: hidden;
    box-shadow: 0 6px 24px rgba(0,0,0,0.25);
  }
  .spread-art {
    position: absolute;
    inset: 0;
    width: 100%;
    height: 100%;
  }
  .brand {
    position: absolute;
    display: flex;
    align-items: center;
    font-family: "Montserrat", sans-serif;
    font-weight: 700;
    color: var(--brand-green);
  }
  .brand-dot {
    border-radius: 50%;
    background: var(--brand-green);
    flex: none;
  }
  .brand--front {
    left: 720px;
    top: 366px;
    font-size: 34px;
    gap: 12px;
  }
  .brand--front .brand-dot { width: 40px; height: 40px; }
  .back-panel-contact {
    position: absolute;
    left: 52px;
    bottom: 58px;
  }
  .brand--back {
    position: static;
    font-size: 21px;
    gap: 8px;
  }
  .brand--back .brand-dot { width: 26px; height: 26px; }
  .contact-lines {
    margin-top: 6px;
    margin-left: 34px;
    font-family: "Montserrat", sans-serif;
    font-weight: 400;
    font-size: 8.5px;
    line-height: 1.45;
    color: var(--contact-grey);
    list-style: none;
  }
</style>
</head>
<body>
<div class="canvas">
  <section class="spread" aria-label="Brochure cover spread: back panel left, front panel right">
    <svg class="spread-art" viewBox="0 0 1080 764" xmlns="http://www.w3.org/2000/svg">
      <defs>
        <radialGradient id="sphereGlow" cx="0.68" cy="0.62" r="0.7">
          <stop offset="0" stop-color="var(--sphere-light)"/>
          <stop offset="1" stop-color="var(--sphere-dark)"/>
        </radialGradient>
      </defs>
      <ellipse class="sphere-decoration" role="img" aria-label="Large faint tiled sphere decoration spanning the fold"
               cx="760" cy="390" rx="370" ry="340" fill="url(#sphereGlow)"/>
      <line class="fold" x1="540" y1="0" x2="540" y2="764" stroke="var(--fold-line)" stroke-width="1"/>
    </svg>

    <div class="back-panel-contact">
      <div class="brand brand--back"><span class="brand-dot"></span><span class="brand-name">Lumivo</span></div>
      <ul class="contact-lines">
        <li>418 Harbor Ave., Suite 310</li>
        <li>Eastfield, NH 03100</li>
        <li>(555) 010-4400</li>
        <li>lumivo.com</li>
      </ul>
    </div>

    <div class="brand brand--front"><span class="brand-dot"></span><span class="brand-name">Lumivo</span></div>
  </section>
</div>
</body>
</html>
```